Seafood company needs a label design

Our brand name is Coral Pilchards. We need a label design for a new product line of 200g trays of sardine fillets. The label/sleeve is going to wrap around the black tray. We are a family owned and operated business in Esperance, Western Australia. We would like simple appealing designs that catch the eye of the consumer.

Target Market(s)

seafood consumers in supermarkets

Colors

Designer to choose colors to be used in the design.

Requirements
Must have
• The front of the label must include
• •Coral Pilchards
• •since 2003
• •Sustainably wild caught from the pristine southern ocean Marlow Cove Western Shores
Nice to have
• Deep/Rich colours, and black, maybe Drawn picture of sardine/sardines or an anchor fast anchor.
Should not have
• cartoon images, not too cluttered

```html
<!DOCTYPE html>
<html lang="en">
<head>
<meta charset="utf-8">
<title>Coral Pilchards – product information</title>
<link href="https://fonts.googleapis.com/css2?family=Open+Sans:wght@400;700&family=Kaushan+Script&display=swap" rel="stylesheet">
<style>
  :root{
    --charcoal:#2b2c2e;
    --charcoal-light:#3a3b3e;
    --teal:#1ea3b8;
    --sky-pale:#e6f4f8;
    --sky:#a9dbe8;
    --ocean:#1579b8;
    --ocean-bright:#2aa7e0;
    --ink:#111214;
    --brand-red:#c8281e;
    --paper:#ffffff;
    --frame:#1f3f6b;
  }
  html,body{margin:0;padding:0;overflow:hidden;background:var(--paper);}
  .label{position:relative;width:1200px;height:308px;overflow:hidden;font-family:"Open Sans",Arial,sans-serif;}
  .label-art{position:absolute;inset:0;}
  .brand-name{
    position:absolute;left:104px;top:74px;width:220px;
    font-family:"Open Sans",Arial,sans-serif;font-weight:700;font-size:30px;line-height:34px;
    color:var(--brand-red);text-align:center;margin:0;
  }
  .info-panel{
    position:absolute;left:673px;top:49px;width:506px;height:134px;box-sizing:border-box;
    background:var(--paper);border:2px solid var(--frame);
    box-shadow:0 0 0 3px rgba(42,167,224,.35),2px 3px 6px rgba(0,0,0,.25);
    display:flex;align-items:center;justify-content:center;padding-left:30px;
  }
  .info-panel p{margin:0;font-size:30px;color:var(--ink);letter-spacing:.3px;}
</style>
</head>
<body>
<div class="label">
  <svg class="label-art" width="1200" height="308" viewBox="0 0 1200 308" xmlns="http://www.w3.org/2000/svg">
    <defs>
      <linearGradient id="sky-wash" x1="0" y1="0" x2="1" y2="0">
        <stop offset="0" stop-color="var(--sky)"/>
        <stop offset=".45" stop-color="var(--sky-pale)"/>
        <stop offset="1" stop-color="#f7fbfc"/>
      </linearGradient>
      <linearGradient id="grilled" x1="0" y1="0" x2="1" y2="1">
        <stop offset="0" stop-color="#b9654a"/><stop offset=".5" stop-color="#6e6a5e"/><stop offset="1" stop-color="#3f3c36"/>
      </linearGradient>
      <linearGradient id="fresh" x1="0" y1="0" x2="1" y2="1">
        <stop offset="0" stop-color="#cfd6d4"/><stop offset=".6" stop-color="#8e9a98"/><stop offset="1" stop-color="#6f9a5a"/>
      </linearGradient>
      <linearGradient id="fried" x1="0" y1="0" x2="1" y2="1">
        <stop offset="0" stop-color="#c9b79a"/><stop offset=".55" stop-color="#8c7a5c"/><stop offset="1" stop-color="#7fa86a"/>
      </linearGradient>
    </defs>

    <!-- frame bands -->
    <rect width="1200" height="308" fill="url(#sky-wash)"/>
    <rect width="1200" height="28" fill="var(--charcoal)"/>
    <rect y="28" width="1200" height="8" fill="var(--teal)"/>

    <!-- ocean swooshes -->
    <path d="M0 250 C300 235 700 250 900 232 C1020 222 1110 205 1200 198 L1200 270 L0 270 Z" fill="var(--charcoal-light)"/>
    <path d="M0 252 C350 248 650 258 860 250 C1000 244 1110 228 1200 220 L1200 232 C1100 240 1000 256 860 262 C650 270 350 262 0 262 Z" fill="var(--ocean-bright)"/>
    <path d="M0 258 C350 256 650 264 860 258 C1000 254 1100 244 1200 236" fill="none" stroke="var(--paper)" stroke-width="2"/>
    <path d="M0 240 C200 236 400 248 600 246" fill="none" stroke="var(--ocean)" stroke-width="10" opacity=".8"/>
    <rect y="270" width="1200" height="8" fill="var(--teal)"/>
    <rect y="278" width="1200" height="30" fill="var(--charcoal)"/>

    <!-- dish photographs -->
    <g role="img" aria-label="Photo of grilled sardines topped with tomato and herbs">
      <circle cx="398" cy="107" r="72" fill="var(--ocean)"/>
      <circle cx="398" cy="107" r="67" fill="url(#grilled)"/>
    </g>
    <g role="img" aria-label="Photo of fresh whole sardines on greens">
      <circle cx="503" cy="145" r="46" fill="var(--ocean)"/>
      <circle cx="503" cy="145" r="41" fill="url(#fresh)"/>
    </g>
    <g role="img" aria-label="Photo of fried sardines served with dipping sauce">
      <circle cx="583" cy="105" r="61" fill="var(--ocean)"/>
      <circle cx="583" cy="105" r="56" fill="url(#fried)"/>
    </g>

    <!-- tagline banner -->
    <rect x="187" y="199" width="632" height="53" fill="var(--ink)"/>
    <text x="196" y="233" textLength="612" lengthAdjust="spacingAndGlyphs"
          font-family="'Kaushan Script', cursive" font-size="21" fill="var(--paper)">Sustainably wild caught from the pristine southern ocean Marlow Cove Western Shores</text>

    <!-- established badge -->
    <circle cx="140" cy="223" r="46" fill="var(--ink)"/>
    <text x="110" y="212" font-family="'Kaushan Script', cursive" font-size="20" fill="var(--paper)">Since</text>
    <text x="106" y="240" font-family="'Kaushan Script', cursive" font-size="25" fill="var(--paper)">2003</text>
  </svg>

  <p class="brand-name">Coral<br>Pilchards</p>

  <div class="info-panel"><p>product information</p></div>
</div>
</body>
</html>
```